I need jar labels, and other types to include round and cigar band with an already designed logo

Need a round sticker to place on products, jar labels, 3 sizes with 1 label having 3 different names. also reflect my design on a thank you card and round sticker
I would like a 10 " cigar band with my logo in the middle for handmade bars of soap

Target Market(s)

This project will be for labeling my products for my e-commerce business

Industry/Entity Type

Beauty

Font styles to use
Serif

Colors
e667a6
ffcf3e

Requirements
Must have
• The labels must contain my logo. I need (4) 1.5" X 4" label with my logo and the words: Handmade Sugar Scrub, Handmade Whipped Body Butter, Handmade Whipped Soap Scrub, Handmade Salt Scrub

I also must have a round sticker 2' in diameter with my logo in Gold

I also need a round sticker I rose gold that reflects my logo and says thank you for supporting my small business.
Nice to have
• I want round and rectangle labels for products that contain my logo. I also need thank you cards and thank you for your order sticker with my logo
Should not have
• do not change the color of my logo and make the print on the labels in Black

```html
<!DOCTYPE html>
<html lang="en">
<head>
<meta charset="utf-8">
<title>Lather and Bloom – Label Set</title>
<link rel="stylesheet" href="https://fonts.googleapis.com/css2?family=Abril+Fatface&family=Great+Vibes&family=Montserrat:wght@400&display=swap">
<style>
  :root {
    --pink: #e667a6;
    --pink-soft: #f6c9df;
    --pink-pale: #fce8f2;
    --rose: #e89ab8;
    --lavender: #e6e5f5;
    --mauve: #e2bedb;
    --mint: #bfe5d6;
    --peach: #f1cfb2;
    --gold: #ffcf3e;
    --gold-deep: #c9a42c;
    --ink: #2b2b2b;
    --rule: #a8a8a8;
    --script-orange: #f08a1c;
    --script-green: #3cc43c;
    --script-magenta: #b0199a;
    --script-violet: #7a4bf0;
    --script-blue: #1f3bd8;
    --display: "Abril Fatface", Georgia, serif;
    --script: "Great Vibes", cursive;
    --ui: "Montserrat", Arial, sans-serif;
  }
  * { box-sizing: border-box; margin: 0; padding: 0; }
  html, body { width: 926px; height: 1200px; overflow: hidden; background: #fff; }
  .sheet { position: relative; width: 926px; height: 1200px; }

  /* dimension marks */
  .dim-line { position: absolute; background: var(--rule); }
  .dim-label { position: absolute; background: #fff; padding: 0 6px; font: 400 11px/1 var(--ui); color: #8a8a8a; }

  /* jar labels */
  .jar-label { position: absolute; left: 71px; width: 447px; height: 166px; overflow: hidden; background: #fff; }
  .label-art { position: absolute; inset: 0; }
  .salt .label-art        { background: linear-gradient(90deg, var(--pink-soft) 0%, #fff 38%, #fff 62%, var(--lavender) 100%); }
  .soap-scrub .label-art  { background: linear-gradient(90deg, var(--peach) 0%, #fff 38%, #fff 62%, var(--mint) 100%); }
  .body-butter .label-art { background: linear-gradient(90deg, var(--pink-pale) 0%, #fff 38%, #fff 62%, var(--lavender) 100%); }
  .sugar .label-art       { background: linear-gradient(90deg, var(--mauve) 0%, #fff 38%, #fff 62%, var(--pink-soft) 100%); }

  .label-copy { position: absolute; left: 110px; top: 8px; width: 228px; display: flex; flex-direction: column; align-items: center; text-align: center; }
  .brand-mark { display: flex; flex-direction: column; align-items: center; gap: 4px; }
  .brand-dot { width: 30px; height: 30px; border-radius: 50%; border: 2px solid var(--gold-deep); }
  .brand-name { font: 400 10px/1 var(--display); color: var(--gold-deep); letter-spacing: .3px; }
  .handmade { font: 400 29px/1 var(--script); margin-top: 14px; }
  .product { font: 400 23px/.86 var(--display); color: var(--gold-deep); margin-top: 2px; }

  /* soap band */
  .soap-band { position: absolute; left: 577px; top: 49px; width: 256px; height: 1109px; overflow: hidden; background: #fff; }
  .band-art { position: absolute; inset: 0;
    background: linear-gradient(180deg, var(--pink-pale) 0%, var(--peach) 35%, #fff 48%, #fff 58%, var(--lavender) 72%, var(--peach) 100%); }
  .band-copy { position: absolute; left: 0; right: 0; top: 500px; display: flex; flex-direction: column; align-items: center; }
  .band-copy .brand-dot { width: 40px; height: 40px; }
  .band-copy .brand-name { font-size: 12px; }
  .band-copy .handmade { margin-top: 14px; font-size: 31px; }

  /* round stickers */
  .sticker { position: absolute; top: 884px; width: 222px; height: 222px; border-radius: 50%; overflow: hidden; background: #fff; }
  .thank-you { left: 62px; }
  .thank-art { position: absolute; inset: 0;
    background: radial-gradient(circle at 50% 50%, #fff 0 52%, var(--pink-soft) 78%, var(--lavender) 100%); }
  .thank-copy { position: absolute; inset: 0; display: flex; flex-direction: column; align-items: center; padding-top: 32px; }
  .thank-copy .brand-dot { border-color: var(--rose); width: 34px; height: 34px; }
  .thank-copy .brand-name { color: var(--rose); }
  .thank-note { margin-top: 12px; font: 400 25px/1.15 var(--script); color: var(--ink); text-align: center; }

  .gold-seal { left: 319px; border: 4px solid var(--gold-deep); display: flex; align-items: center; justify-content: center; }
  .gold-seal .brand-name { font-size: 26px; line-height: 1.05; text-align: center; }
</style>
</head>
<body>
<main class="sheet">

  <!-- dimensions: jar labels -->
  <div class="dim-line" style="left:71px;top:36px;width:447px;height:1px;"></div>
  <div class="dim-line" style="left:71px;top:26px;width:1px;height:20px;"></div>
  <div class="dim-line" style="left:517px;top:26px;width:1px;height:20px;"></div>
  <span class="dim-label" style="left:280px;top:31px;">4”</span>

  <div class="dim-line" style="left:531px;top:49px;width:1px;height:166px;"></div>
  <div class="dim-line" style="left:521px;top:49px;width:20px;height:1px;"></div>
  <div class="dim-line" style="left:521px;top:214px;width:20px;height:1px;"></div>
  <span class="dim-label" style="left:522px;top:125px;padding:3px 1px;">1.5”</span>

  <!-- dimensions: soap band -->
  <div class="dim-line" style="left:577px;top:36px;width:256px;height:1px;"></div>
  <div class="dim-line" style="left:577px;top:26px;width:1px;height:20px;"></div>
  <div class="dim-line" style="left:832px;top:26px;width:1px;height:20px;"></div>
  <span class="dim-label" style="left:685px;top:31px;">2,3”</span>

  <div class="dim-line" style="left:848px;top:49px;width:1px;height:1109px;"></div>
  <div class="dim-line" style="left:838px;top:49px;width:20px;height:1px;"></div>
  <div class="dim-line" style="left:838px;top:1157px;width:20px;height:1px;"></div>
  <span class="dim-label" style="left:838px;top:598px;padding:4px 1px;">10”</span>

  <!-- dimensions: stickers -->
  <div class="dim-line" style="left:62px;top:1123px;width:222px;height:1px;"></div>
  <div class="dim-line" style="left:62px;top:1100px;width:1px;height:30px;"></div>
  <div class="dim-line" style="left:283px;top:1100px;width:1px;height:30px;"></div>
  <span class="dim-label" style="left:160px;top:1118px;">2”</span>

  <div class="dim-line" style="left:319px;top:1123px;width:222px;height:1px;"></div>
  <div class="dim-line" style="left:319px;top:1100px;width:1px;height:30px;"></div>
  <div class="dim-line" style="left:540px;top:1100px;width:1px;height:30px;"></div>
  <span class="dim-label" style="left:417px;top:1118px;">2”</span>

  <!-- jar labels -->
  <section class="jar-label salt" style="top:48px;">
    <div class="label-art" role="img" aria-label="Abstract pastel shape artwork"></div>
    <div class="label-copy">
      <div class="brand-mark"><span class="brand-dot"></span><span class="brand-name">Lather and Bloom</span></div>
      <p class="handmade" style="color:var(--script-orange);">handmade</p>
      <h2 class="product">salt<br>scrub</h2>
    </div>
  </section>

  <section class="jar-label soap-scrub" style="top:239px;">
    <div class="label-art" role="img" aria-label="Abstract pastel shape artwork"></div>
    <div class="label-copy">
      <div class="brand-mark"><span class="brand-dot"></span><span class="brand-name">Lather and Bloom</span></div>
      <p class="handmade" style="color:var(--script-green);">handmade</p>
      <h2 class="product">whipped soap<br>scrub</h2>
    </div>
  </section>

  <section class="jar-label body-butter" style="top:424px;">
    <div class="label-art" role="img" aria-label="Abstract pastel shape artwork"></div>
    <div class="label-copy">
      <div class="brand-mark"><span class="brand-dot"></span><span class="brand-name">Lather and Bloom</span></div>
      <p class="handmade" style="color:var(--script-magenta);">handmade</p>
      <h2 class="product">whipped body<br>butter</h2>
    </div>
  </section>

  <section class="jar-label sugar" style="top:609px;">
    <div class="label-art" role="img" aria-label="Abstract pastel shape artwork"></div>
    <div class="label-copy">
      <div class="brand-mark"><span class="brand-dot"></span><span class="brand-name">Lather and Bloom</span></div>
      <p class="handmade" style="color:var(--script-violet);">handmade</p>
      <h2 class="product">sugar<br>scrub</h2>
    </div>
  </section>

  <!-- soap cigar band -->
  <section class="soap-band">
    <div class="band-art" role="img" aria-label="Abstract pastel shape artwork"></div>
    <div class="band-copy">
      <div class="brand-mark"><span class="brand-dot"></span><span class="brand-name">Lather and Bloom</span></div>
      <p class="handmade" style="color:var(--script-blue);">handmade</p>
      <h2 class="product">soap</h2>
    </div>
  </section>

  <!-- thank you sticker -->
  <section class="sticker thank-you">
    <div class="thank-art" role="img" aria-label="Abstract pastel shape artwork around the sticker edge"></div>
    <div class="thank-copy">
      <div class="brand-mark"><span class="brand-dot"></span><span class="brand-name">Lather and Bloom</span></div>
      <p class="thank-note">Thank you<br>for supporting my<br>small business!</p>
    </div>
  </section>

  <!-- gold brand sticker -->
  <section class="sticker gold-seal">
    <span class="brand-name">Lather<br>and Bloom</span>
  </section>

</main>
</body>
</html>
```